Verlane Supply Chain and Logistic Consulting

Please review the attached Business Card. I want as close to this card with the colors, fonts, and quality of the card as possible. The attached compass should replace the deer head on both sides of the card and the text should say:

Backside
Compass JPEG
Verlane SC&L
A Supply Chain and Logistics Consulting Company

Frontside
Verlane SC&L
Ross Quillam - Brisport Coast
President
____________________________________
(555) 314-2960
VerlaneSCL@Mailbrook.com
_____________________________________

Bottom Front Side

Target Market(s)

Businesses

Contact Information for Business Card

Backside
Compass JPEG
Verlane SC&L

Frontside
Verlane SC&L
President
(555) 314-2960
VerlaneSCL@Mailbrook.com

Bottom Front Side

Font styles to use
Serif
Script

Colors

Designer to choose colors to be used in the design.

Requirements
Must have
• See attached card for reference
Nice to have
Should not have

```html
<!DOCTYPE html>
<html lang="en">
<head>
<meta charset="utf-8">
<title>Verlane SC&amp;L Business Card</title>
<link href="https://fonts.googleapis.com/css2?family=Domine:wght@400&family=Cormorant+Garamond:wght@400;500&family=Roboto:wght@400&display=swap" rel="stylesheet">
<style>
  :root {
    --canvas: #ffffff;
    --card: #252525;
    --ink: #ffffff;
    --muted: #c4c4c4;
    --rule: #9a9a9a;
    --ghost: #2f2f2f;
    --mark: #d8d8d8;
  }
  * { margin: 0; padding: 0; box-sizing: border-box; }
  html, body { width: 1200px; height: 1000px; overflow: hidden; background: var(--canvas); }
  .canvas { position: relative; width: 1200px; height: 1000px; }
  .card {
    position: absolute;
    width: 754px;
    height: 422px;
    background: var(--card);
    overflow: hidden;
  }
  .card--back { left: 53px; top: 51px; }
  .card--front { left: 391px; top: 523px; }
  .centered { position: absolute; left: 0; width: 100%; text-align: center; line-height: 1; white-space: nowrap; }
  .brand-mark { position: absolute; left: 295px; top: 72px; }
  .brand-name { font-family: "Domine", Georgia, serif; font-weight: 400; color: var(--ink); font-size: 36px; letter-spacing: 0.5px; }
  .tagline { font-family: "Roboto", Arial, sans-serif; font-weight: 400; color: var(--muted); font-size: 12px; letter-spacing: 1.1px; text-transform: uppercase; }
  .card--back .brand-name { top: 259px; }
  .card--back .tagline { top: 300px; }
  .front-ghost { position: absolute; left: 401px; top: -5px; }
  .card--front .brand-name { top: 69px; }
  .card--front .tagline { top: 117px; }
  .card--front .footer-tagline { top: 383px; }
  .person, .role, .contact { font-family: "Cormorant Garamond", Georgia, serif; color: var(--ink); }
  .person { top: 164px; font-size: 29px; }
  .role { top: 206px; font-size: 21px; }
  .contact { font-size: 21px; }
  .contact--phone { top: 275px; }
  .contact--email { top: 310px; }
  .divider {
    position: absolute; left: 205px; top: 256px; width: 295px; height: 1px;
    background: linear-gradient(90deg, transparent, #e0e0e0 55%, transparent);
  }
  .footer-rule { position: absolute; top: 389px; height: 1px; background: var(--rule); width: 176px; }
  .footer-rule--left { left: 20px; }
  .footer-rule--right { left: 562px; }
</style>
</head>
<body>
<div class="canvas">
  <section class="card card--back">
    <svg class="brand-mark" width="166" height="166" viewBox="0 0 166 166" aria-hidden="true">
      <circle cx="83" cy="83" r="80" fill="none" stroke="var(--mark)" stroke-width="2"/>
    </svg>
    <div class="centered brand-name">VERLANE SC&amp;L</div>
    <div class="centered tagline">A Supply Chain and Logistics Consulting Company</div>
  </section>

  <section class="card card--front">
    <svg class="front-ghost" width="450" height="450" viewBox="0 0 450 450" aria-hidden="true">
      <circle cx="225" cy="225" r="224" fill="var(--ghost)"/>
    </svg>
    <div class="centered brand-name">VERLANE SC&amp;L</div>
    <div class="centered tagline">A Supply Chain and Logistics Consulting Company</div>
    <div class="centered person">Ross Quillam • Brisport Coast</div>
    <div class="centered role">President</div>
    <div class="divider"></div>
    <div class="centered contact contact--phone">(555) 314-2960</div>
    <div class="centered contact contact--email">VerlaneSCL@Mailbrook.com</div>
    <div class="footer-rule footer-rule--left"></div>
    <div class="centered tagline footer-tagline">A Supply Chain and Logistics Consulting Company</div>
    <div class="footer-rule footer-rule--right"></div>
  </section>
</div>
</body>
</html>
```